Marta Gellworth Name Card Design

Hello Designers,
I wanna have a name card with these details below:
Name: Marta Gellworth
Job Title: Doctor
Address: 2318 Birch Lane, Tacoma, WA, US
Phone: 9517380294
Slogan on card: Health care 24/7, Whenever you need, we're there!
I love yellows colors, red and white. It would be nice if my card would be designed with these colors.

Doctor

```html
<!DOCTYPE html>
<html lang="en">
<head>
<meta charset="utf-8">
<title>Marta Gellworth – Name Card</title>
<link rel="stylesheet" href="https://fonts.googleapis.com/css2?family=Arimo:wght@400;700&family=Roboto+Condensed:wght@700&display=swap">
<style>
  :root {
    --card-yellow: #fbdc00;
    --cross-red: #d9261c;
    --text-white: #ffffff;
    --text-yellow: #fbdc00;
  }
  html, body {
    margin: 0;
    padding: 0;
    overflow: hidden;
    background: #ffffff;
  }
  .card {
    position: relative;
    width: 1200px;
    height: 686px;
    background: var(--card-yellow);
    overflow: hidden;
    font-family: "Arimo", Arial, sans-serif;
  }
  .cross-bar {
    position: absolute;
    background: var(--cross-red);
  }
  .cross-bar--vertical {
    left: 257px;
    width: 689px;
    top: 0;
    height: 686px;
  }
  .cross-bar--horizontal {
    left: 0;
    width: 1200px;
    top: 185px;
    height: 312px;
  }
  .line {
    position: absolute;
    left: 257px;
    width: 689px;
    margin: 0;
    text-align: center;
    white-space: pre;
  }
  .doctor-name {
    top: 104px;
    font-size: 31px;
    font-weight: 400;
    color: var(--text-white);
  }
  .headline {
    top: 286px;
    font-size: 63px;
    font-weight: 700;
    color: var(--text-yellow);
    letter-spacing: 0.5px;
  }
  .tagline {
    top: 352px;
    font-family: "Roboto Condensed", "Arial Narrow", sans-serif;
    font-size: 42px;
    font-weight: 700;
    color: var(--text-yellow);
  }
  .address {
    top: 535px;
    font-size: 32px;
    font-weight: 700;
    color: var(--text-white);
  }
  .phone {
    top: 588px;
    font-size: 46px;
    font-weight: 700;
    color: var(--text-white);
    letter-spacing: 2px;
  }
</style>
</head>
<body>
  <div class="card">
    <div class="cross-bar cross-bar--vertical"></div>
    <div class="cross-bar cross-bar--horizontal"></div>

    <p class="line doctor-name">Dr. Marta Gellworth</p>
    <h1 class="line headline">Health Care 24/7</h1>
    <p class="line tagline">Whenever you need, we're there!</p>
    <p class="line address">2318 Birch Lane, Tacoma, WA, US</p>
    <p class="line phone">Phone  :  9517380294</p>
  </div>
</body>
</html>
```